Rehab/fitness Business card design

I need a design that promotes "A ready made base for runners". services include assessment, massage, physiotherapy, pilates, suspension training, kinesiotaping in any combination.
I would like to bring the design into my website, flyers etc

Target Market(s)

athletes from beginner to elite - any age, male and female

Industry/Entity Type

Shop

Contact Information for Business Card

Ready-Made-Base for Runners
17 Parvel Crescent, Hollowmere, Tauranga
021 847 3610
gwen.farrowby@quillmail.test

Logo Text

Requirements
Nice to have
• Blue colour theme

```html
<!DOCTYPE html>
<html lang="en">
<head>
<meta charset="utf-8">
<title>Ready Made Base for Runners — Business Card</title>
<link rel="stylesheet" href="https://fonts.googleapis.com/css2?family=Oswald:wght@700&family=Jost:wght@400;500&display=swap">
<style>
  :root {
    --ink: #231f20;
    --blue: #0a9be0;
    --white: #ffffff;
    --page: #e9e9e9;
  }
  html, body {
    margin: 0;
    width: 1200px;
    height: 1000px;
    overflow: hidden;
    background: var(--page);
  }
  .canvas {
    position: relative;
    width: 1200px;
    height: 1000px;
  }
  .card {
    position: absolute;
    left: 210px;
    width: 780px;
    height: 440px;
    background: var(--ink);
    border-radius: 34px;
    overflow: hidden;
    font-family: "Jost", sans-serif;
  }
  .card--front { top: 40px; }
  .card--back  { top: 520px; }

  /* Front */
  .front__rule {
    position: absolute;
    left: 0; right: 0; top: 44px;
    height: 4px;
    background: var(--blue);
  }
  .brand {
    position: absolute;
    left: 70px; top: 118px;
    display: flex;
    align-items: center;
    gap: 14px;
  }
  .brand__dot {
    width: 46px; height: 46px;
    border-radius: 50%;
    background: var(--blue);
  }
  .brand__name {
    font-family: "Oswald", sans-serif;
    font-weight: 700;
    font-size: 44px;
    letter-spacing: 0.5px;
    color: var(--blue);
    text-transform: uppercase;
    line-height: 1;
  }
  .address {
    position: absolute;
    left: 300px; top: 190px;
    margin: 0;
    font-style: normal;
    font-size: 25px;
    line-height: 1.45;
    letter-spacing: 1px;
    color: var(--blue);
  }
  .contact-band {
    position: absolute;
    left: 0; right: 0; top: 326px;
    height: 70px;
    background: var(--blue);
    display: flex;
    align-items: center;
    justify-content: space-between;
    padding: 0 56px 0 64px;
    color: var(--white);
    font-size: 25px;
    letter-spacing: 0.5px;
  }
  .contact-band__phone span { letter-spacing: 2px; }

  /* Back */
  .back__panel {
    position: absolute;
    left: 0; top: 0;
    width: 360px; height: 440px;
  }
  .services-label {
    position: absolute;
    left: 346px; top: 36px;
    width: 30px;
    margin: 0;
    display: flex;
    flex-direction: column;
    align-items: center;
    color: var(--white);
    font-size: 30px;
    line-height: 38px;
  }
  .services-rule {
    position: absolute;
    left: 392px; top: 44px;
    width: 3px; height: 330px;
    background: var(--blue);
  }
  .services-list {
    position: absolute;
    left: 420px; top: 36px;
    margin: 0; padding: 0;
    list-style: none;
    color: var(--blue);
    font-size: 27px;
    line-height: 47px;
    letter-spacing: 0.5px;
  }
</style>
</head>
<body>
<main class="canvas">

  <section class="card card--front" aria-label="Business card front">
    <div class="front__rule"></div>
    <div class="brand">
      <div class="brand__dot"></div>
      <h1 class="brand__name">Ready Made Base for Runners</h1>
    </div>
    <address class="address">
      17 Parvel Crescent,<br>
      Hollowmere,<br>
      Tauranga
    </address>
    <div class="contact-band">
      <span class="contact-band__phone">Phone <span>021 847 3610</span></span>
      <span class="contact-band__email">gwen.farrowby@quillmail.test</span>
    </div>
  </section>

  <section class="card card--back" aria-label="Business card back">
    <svg class="back__panel" viewBox="0 0 360 440" role="img" aria-label="Running athlete silhouette on blue panel">
      <path d="M0 0 H250 C335 70 350 300 225 440 H0 Z" fill="var(--blue)"/>
    </svg>
    <p class="services-label" aria-label="services">
      <span>s</span><span>e</span><span>r</span><span>v</span><span>i</span><span>c</span><span>e</span><span>s</span>
    </p>
    <div class="services-rule"></div>
    <ul class="services-list">
      <li>Assessment</li>
      <li>Massage</li>
      <li>Physiotherapy</li>
      <li>Pilates</li>
      <li>Suspension training</li>
      <li>Kinesiotaping</li>
      <li>in any combination.</li>
    </ul>
  </section>

</main>
</body>
</html>
```